Bramblefield Circle for Nurses - New facebook banner design + logo

We are setting up a new private facebook group called Bramblefield Circle for Nurses. Administered by Marla Teske, Marla helps women in healthcare to crush their life and health goals so they can bring their best version of themselves to others. We would like a modern / contemporary header design incorporating colours / fonts from the attached moodboard. An icon or image representing a woman. Our initial thinking included an icon of a woman outline? Just thoughts. Bright bold colours incorporating some gold / marble. See existing business brandboard however elements of Bramblefield Circle for Nurses DO NOT need to be aligned to this brandboard. Images should represent personal strength (not physical strength ie. fitness), community and femininity.

Target Market(s)

Women in healthcare

Industry/Entity Type

Healthcare

Font styles to use
Sans Serif

Requirements
Must have
• unique iconology that can be used to represent the group. I've attached some examples of woman silhouettes. Doesn't need to be full body but iconology may just include head / shoulders / torso.

```html
<!DOCTYPE html>
<html lang="en">
<head>
<meta charset="utf-8">
<title>Bramblefield Circle for Nurses – Group Banner</title>
<link rel="stylesheet" href="https://fonts.googleapis.com/css2?family=Montserrat:wght@700&family=Alex+Brush&display=swap">
<style>
  :root {
    --stage: #5d5956;
    --cream: #e1d9bf;
    --teal-bright: #00a9b2;
    --teal-light: #1bb9bf;
    --teal-mid: #0b97a2;
    --teal-deep: #005a70;
    --teal-vein: #04707f;
    --gold-light: #f6e6a6;
    --gold: #c9a24a;
    --gold-dark: #8c6a22;
    --ink: #1f1f1f;
    --white: #ffffff;
  }
  * { margin: 0; padding: 0; box-sizing: border-box; }
  html, body {
    width: 1200px;
    height: 1000px;
    overflow: hidden;
    background: var(--stage);
  }
  .banner {
    position: absolute;
    left: 123px;
    top: 231px;
    width: 954px;
    height: 498px;
    overflow: hidden;
  }
  .banner__art {
    position: absolute;
    inset: 0;
    width: 100%;
    height: 100%;
    display: block;
  }
  .banner__title-block {
    position: absolute;
    left: 400px;
    width: 550px;
    top: 193px;
    text-align: center;
    color: var(--white);
  }
  .banner__title {
    font-family: "Montserrat", Arial, sans-serif;
    font-weight: 700;
    font-size: 33px;
    line-height: 46px;
    letter-spacing: 0.3px;
    text-transform: uppercase;
  }
  .banner__byline {
    font-family: "Alex Brush", cursive;
    font-size: 36px;
    line-height: 44px;
    margin-top: 6px;
  }
</style>
</head>
<body>
  <section class="banner" aria-label="Bramblefield Circle for Nurses group banner">
    <svg class="banner__art" viewBox="0 0 954 498" xmlns="http://www.w3.org/2000/svg">
      <defs>
        <linearGradient id="gold-line" x1="0" x2="1" y1="0" y2="0">
          <stop offset="0" stop-color="#b48a34"/>
          <stop offset="0.25" stop-color="#f6e6a6"/>
          <stop offset="0.55" stop-color="#c9a24a"/>
          <stop offset="0.8" stop-color="#f6e6a6"/>
          <stop offset="1" stop-color="#c9a24a"/>
        </linearGradient>
        <linearGradient id="gold-ring" x1="0" x2="0" y1="0" y2="1">
          <stop offset="0" stop-color="#f6e6a6"/>
          <stop offset="0.5" stop-color="#c9a24a"/>
          <stop offset="1" stop-color="#8c6a22"/>
        </linearGradient>
        <linearGradient id="teal-ring" x1="0" x2="0" y1="0" y2="1">
          <stop offset="0" stop-color="#1bb9bf"/>
          <stop offset="0.5" stop-color="#0b97a2"/>
          <stop offset="1" stop-color="#1bb9bf"/>
        </linearGradient>
        <linearGradient id="deep-band" x1="0" x2="0" y1="0" y2="1">
          <stop offset="0" stop-color="#066c80"/>
          <stop offset="0.5" stop-color="#005a70"/>
          <stop offset="1" stop-color="#05687c"/>
        </linearGradient>
        <radialGradient id="marble-a" cx="0.35" cy="0.2" r="0.6">
          <stop offset="0" stop-color="#2cc1c6" stop-opacity="0.7"/>
          <stop offset="1" stop-color="#2cc1c6" stop-opacity="0"/>
        </radialGradient>
        <radialGradient id="marble-b" cx="0.75" cy="0.85" r="0.5">
          <stop offset="0" stop-color="#04848f" stop-opacity="0.45"/>
          <stop offset="1" stop-color="#04848f" stop-opacity="0"/>
        </radialGradient>
        <radialGradient id="marble-c" cx="0.6" cy="0.5" r="0.5">
          <stop offset="0" stop-color="#0b7f95" stop-opacity="0.55"/>
          <stop offset="1" stop-color="#0b7f95" stop-opacity="0"/>
        </radialGradient>
        <linearGradient id="figure-tone" x1="0" x2="1" y1="0" y2="1">
          <stop offset="0" stop-color="#2a2a2a"/>
          <stop offset="0.45" stop-color="#1f1f1f"/>
          <stop offset="0.6" stop-color="#8a7336"/>
          <stop offset="0.72" stop-color="#1f1f1f"/>
          <stop offset="1" stop-color="#1f1f1f"/>
        </linearGradient>
        <clipPath id="medallion-clip">
          <circle cx="40" cy="249" r="325"/>
        </clipPath>
      </defs>

      <!-- teal field with soft marble wash -->
      <rect class="field" x="0" y="0" width="954" height="498" fill="var(--teal-bright)"/>
      <rect class="field-marble" x="300" y="27" width="654" height="444" fill="var(--teal-bright)"/>
      <rect class="field-marble" x="300" y="27" width="654" height="444" fill="url(#marble-a)"/>
      <rect class="field-marble" x="300" y="27" width="654" height="444" fill="url(#marble-b)"/>

      <!-- deep central band -->
      <rect class="band" x="300" y="152" width="654" height="218" fill="url(#deep-band)"/>
      <rect class="band-marble" x="300" y="152" width="654" height="218" fill="url(#marble-c)"/>

      <!-- gold rules -->
      <rect class="rule" x="300" y="132" width="654" height="3" fill="url(#gold-line)"/>
      <rect class="rule" x="300" y="145" width="654" height="5" fill="url(#gold-line)"/>
      <rect class="rule" x="300" y="372" width="654" height="5" fill="url(#gold-line)"/>
      <rect class="rule" x="300" y="387" width="654" height="3" fill="url(#gold-line)"/>

      <!-- cream medallion with rings -->
      <circle class="ring-teal" cx="40" cy="249" r="345" fill="url(#teal-ring)"/>
      <circle class="ring-gold" cx="40" cy="249" r="334" fill="url(#gold-ring)"/>
      <circle class="medallion" cx="40" cy="249" r="325" fill="var(--cream)"/>

      <!-- figure illustration area -->
      <g clip-path="url(#medallion-clip)">
        <rect class="figure-area" role="img"
              aria-label="Illustration area: black silhouette of a confident woman with long hair raising her fist, holding a gold folder at her side"
              x="30" y="40" width="275" height="470" rx="90" ry="90"
              fill="url(#figure-tone)"/>
      </g>
    </svg>

    <div class="banner__title-block">
      <h1 class="banner__title">Bramblefield Circle<br>for Nurses</h1>
      <p class="banner__byline">By Marla Teske</p>
    </div>
  </section>
</body>
</html>
```